Design a Website Mockup for Veltrane Medical Ltd

Veltrane Medical Ltd is a research and medical practice for new radiotherapy treatments for treating pancreatic cancer.

The site can be similar in look and feel to www.quorivant.example.

This site represents trust, hope and the best in medical care and I need the design to reflect this.

I have attached the logo (one with a tag line and one without) to be included in the site. The site should be branded around this logo. I do not want the site to be entirely purple. I am looking for sleek, sophisticated ways to integrate this purple logo.

Below is a summary of what the website will include:

Things to be on the front page:
About Us
Products
Technology
Clinical Trials
Investors
Newsroom
Box to quickly enter email address to join mailing list
Text - introducing Veltrane Medical
Animation about the technology - will be produced separately later on.

Tabs to be on every page so should be in a logical place to remain on every screen page.
Home
Contact Us
Join Us (Careers/investors)
Follow Us (Newsletter/social media/subscribe and archive)

Links at the bottom
Privacy Policy
FAQs
Disclaimer
Webmail
Sitemap

The text that should be included for right now however this will likely change should be:

Veltrane Medical is a global life-sciences company that develops and delivers effective oncology treatments using novel small particle technology. This effective new treatment delivers Selective Internal Radiation Therapy directly into the pancreas. Veltrane Medical Ltd is dedicated to delivering the latest innovations in radiotherapy treatments to ensure quality of life and the best possible care for pancreatic cancer patients. Veltrane Medical is utilising new technology to deliver safer radiotherapy treatments.

```html
<!DOCTYPE html>
<html lang="en">
<head>
<meta charset="utf-8">
<title>Veltrane Medical Ltd</title>
<link href="https://fonts.googleapis.com/css2?family=PT+Sans+Narrow:wght@400;700&family=PT+Sans:wght@400;700&family=Kalam&display=swap" rel="stylesheet">
<style>
:root{
  --purple:#4a0f5f;
  --purple-bright:#8a2fb8;
  --ink:#222;
  --muted:#555;
  --light:#f2f2f2;
  --line:#d6d6d6;
  --orange:#f26522;
  --orange-light:#ff8a3d;
  --footer:#000;
  --footer-text:#9a9a9a;
}
*{box-sizing:border-box;margin:0;padding:0}
html,body{width:1033px;height:1200px;overflow:hidden;background:#fff}
body{font-family:"PT Sans",Verdana,sans-serif;color:var(--ink)}
.page{position:relative;width:1033px;height:1200px;overflow:hidden;background:linear-gradient(#fff 0,#fff 140px,#f3f3f3 260px,#fff 420px)}
.abs{position:absolute}

/* header */
.header{left:0;top:0;width:1033px;height:107px;background:linear-gradient(#fdfdfd,#e9e9e9);border-top:2px solid var(--purple)}
.brand{left:152px;top:34px;display:flex;align-items:center;gap:9px}
.brand-dot{width:30px;height:30px;border-radius:50%;background:var(--purple-bright);flex:0 0 auto}
.brand-name{font-family:"PT Sans",sans-serif;font-weight:700;font-size:22px;color:var(--purple-bright);line-height:1}
.connect{left:528px;top:12px;font-family:"Kalam",cursive;font-size:19px;color:#555}
.call{left:717px;top:12px;font-family:"Kalam",cursive;font-size:18px;color:#555}
.social{left:498px;top:46px;display:flex;gap:5px}
.social span{width:26px;height:26px;border-radius:4px;display:block;box-shadow:inset 0 -3px 0 rgba(0,0,0,.15)}
.search{left:720px;top:46px;width:171px;height:27px;border:2px solid #8f6fb0;border-radius:4px;background:#fff;font-size:13px;color:#555;padding:4px 8px}
.search svg{position:absolute;right:6px;top:4px}

/* nav */
.nav{left:0;top:107px;width:1033px;height:24px;background:var(--purple);display:flex;padding-left:184px}
.nav a{font-family:"PT Sans Narrow",sans-serif;font-size:14.5px;color:#e6dced;text-decoration:none;line-height:24px;padding:0 9px;letter-spacing:.2px}
.nav a.active{background:#000;color:#fff;padding:0 12px}

.headline{left:0;top:148px;width:1033px;text-align:center;font-family:"PT Sans Narrow",sans-serif;font-size:24px;font-weight:400;color:#111}

/* slider */
.slider{left:142px;top:194px;width:749px;height:243px;border:1px solid #ccc;display:flex;box-shadow:0 8px 10px -6px rgba(0,0,0,.3)}
.slide-a{width:375px;height:100%;background:linear-gradient(135deg,#e9ecef,#b9c0c6 55%,#8aa7b8)}
.slide-b{flex:1;height:100%;background:linear-gradient(135deg,#cfd9df,#6f8aa0 55%,#e5eaee)}
.arrow{top:287px;width:26px;height:44px;background:#d4d4d4}
.arrow.left{left:119px;border-radius:22px 0 0 22px}
.arrow.right{left:891px;border-radius:0 22px 22px 0}
.dots{left:459px;top:449px;display:flex;gap:6px}
.dots i{width:12px;height:12px;border-radius:50%;background:radial-gradient(circle at 40% 35%,#ffe07a,#f0a020)}
.dots i.on{background:radial-gradient(circle at 40% 35%,#8a55b5,var(--purple))}

/* intro */
.intro-title{left:142px;top:487px;font-family:"PT Sans Narrow",sans-serif;font-size:19px;font-weight:400;color:#111}
.intro-text{left:142px;top:516px;width:457px;font-family:Verdana,sans-serif;font-size:12px;line-height:15px;text-align:justify;color:#222}
.intro-text a{color:var(--orange)}

/* signup */
.signup{left:634px;top:494px;width:257px;height:137px;border:1px solid #ccc;border-radius:4px;background:linear-gradient(#f8f8f8,#ebebeb)}
.signup .mail{left:13px;top:10px;width:63px;height:58px;border:1px solid #bbb;border-radius:4px;background:#fff}
.signup h3{left:90px;top:6px;font-family:"PT Sans Narrow",sans-serif;font-size:19px;font-weight:400;color:#111}
.signup input{position:absolute;left:90px;width:152px;height:25px;border:1px solid #bbb;font-size:11.5px;padding:0 6px;font-family:Verdana,sans-serif;color:#333;background:#fff}
.signup .perk{left:16px;font-size:11.5px;color:#111;font-family:Verdana,sans-serif;display:flex;align-items:center;gap:5px}
.btn{background:linear-gradient(var(--orange-light),var(--orange));color:#fff;font-family:"PT Sans Narrow",sans-serif;font-size:14px;border-radius:4px;text-align:center;border:1px solid #d4501a}
.signup .btn{left:170px;top:102px;width:72px;height:25px;line-height:23px}

/* videos */
.tab{left:150px;top:674px;width:122px;height:27px;border:1px solid #ccc;border-bottom:none;border-radius:4px 4px 0 0;background:#f4f4f4;font-family:"PT Sans Narrow",sans-serif;font-size:16px;text-align:center;line-height:27px;color:#111}
.more-link{left:532px;top:680px;font-family:Verdana,sans-serif;font-size:12px;color:#e0201a}
.video-panel{left:142px;top:700px;width:451px;height:262px;border:1px solid #ccc;border-radius:0 4px 4px 4px;background:#efefef}
.video{left:162px;top:721px;width:314px;height:223px;background:linear-gradient(135deg,#d7dee5,#5e7f99 50%,#2f4a66);border:1px solid #999}
.video-bar{left:162px;top:930px;width:314px;height:14px;background:#e9e9e9;border-top:1px solid #999;font-size:8px;line-height:13px;padding-left:6px;color:#333;white-space:nowrap;overflow:hidden}
.play{left:298px;top:803px;width:36px;height:36px;border-radius:50%;background:rgba(255,255,255,.85)}
.thumb{left:498px;width:76px;height:38px;border:2px solid #777;border-radius:4px;background:linear-gradient(135deg,#c9d3db,#6d8599)}

/* services */
.services-title{left:634px;top:674px;width:257px;height:30px;border-bottom:1px solid #bbb;display:flex;align-items:center;gap:10px}
.services-title h2{font-family:"PT Sans Narrow",sans-serif;font-weight:400;font-size:21px;color:#111}
.service{left:642px;width:246px;display:flex;gap:10px;font-family:Verdana,sans-serif;font-size:10.5px;line-height:12.5px;color:#111}
.service a{color:var(--orange)}
.service .ico{flex:0 0 14px;height:13px;border:1px solid #888;background:#fff;position:relative;margin-top:2px}
.service .ico:after{content:"";position:absolute;right:-3px;bottom:-3px;width:8px;height:8px;border-radius:50%;background:#3aa238}
.services .btn{left:792px;top:921px;width:84px;height:25px;line-height:23px;font-size:13px}

/* footer */
.footer{left:0;top:1007px;width:1033px;height:193px;background:var(--footer);color:var(--footer-text)}
.footer .ask{left:142px;top:12px;font-family:"PT Sans Narrow",sans-serif;font-size:18px;line-height:21px;color:#9e9e9e}
.footer .f-brand{left:143px;top:84px;display:flex;align-items:center;gap:8px}
.footer .f-brand .brand-name{font-size:17px;line-height:18px}
.footer .f-brand .brand-dot{width:24px;height:24px}
.office{left:271px;top:80px;font-family:Verdana,sans-serif;font-size:10.5px;line-height:14px}
.office b{color:#aaa}
.contact-grid{left:271px;top:116px;display:grid;grid-template-columns:56px 125px 44px 130px;row-gap:3px;font-family:Verdana,sans-serif;font-size:10.5px;color:#ddd}
.contact-grid b{font-weight:700;color:#fff}
.qn-title{left:636px;top:22px;font-family:"PT Sans Narrow",sans-serif;font-size:18px;color:#9e9e9e}
.qn{top:56px;list-style:none;font-family:Verdana,sans-serif;font-size:11px;line-height:15px;color:#777}
.qn li:before{content:"→ ";color:#666;margin-right:6px}
.copyright{left:150px;top:172px;font-family:Verdana,sans-serif;font-size:10.5px;color:#fff}
.copyright a{color:#9b6bd1;margin-left:10px}
</style>
</head>
<body>
<div class="page">

  <header class="header abs">
    <div class="brand abs"><span class="brand-dot"></span><span class="brand-name">Veltrane Medical</span></div>
    <div class="connect abs">← Connect with us</div>
    <div class="call abs">Call: 000 4821 3307</div>
    <div class="social abs" aria-label="Social links">
      <span style="background:#2fa8d6"></span><span style="background:#3b5998"></span><span style="background:#2b7bb0"></span><span style="background:#2f67b0"></span><span style="background:#d43a2f"></span><span style="background:#f07c1f"></span><span style="background:#e4e4e4;border:1px solid #bbb"></span>
    </div>
    <div class="search abs">Search...
      <svg width="16" height="16" viewBox="0 0 16 16"><circle cx="8" cy="8" r="7.5" fill="#7a2fa8"/><circle cx="7.5" cy="7.5" r="3" fill="none" stroke="#fff" stroke-width="1.6"/><line x1="9.7" y1="9.7" x2="12" y2="12" stroke="#fff" stroke-width="1.8"/></svg>
    </div>
  </header>

  <nav class="nav abs">
    <a class="active" href="#">HOME</a><a href="#">ABOUT US</a><a href="#">PRODUCTS</a><a href="#">TECHNOLOGY</a><a href="#">CLINICAL TRIALS</a><a href="#">INVESTORS</a><a href="#">NEWSROOM</a><a href="#">JOIN US</a><a href="#">CONTACT US</a>
  </nav>

  <h1 class="headline abs">NEW TECHNOLOGY TO PROVIDE SAFER RADIOTHERAPY TREATMENTS</h1>

  <div class="arrow left abs"></div>
  <div class="arrow right abs"></div>
  <div class="slider abs">
    <div class="slide-a" role="img" aria-label="Photo of a patient being prepared for radiotherapy by clinical staff"></div>
    <div class="slide-b" role="img" aria-label="Photo of clinicians reviewing scans on monitors in a treatment control room"></div>
  </div>
  <div class="dots abs"><i class="on"></i><i></i><i></i><i></i><i></i><i></i></div>

  <h2 class="intro-title abs">WHO WE ARE?</h2>
  <p class="intro-text abs">Veltrane Medical is a global life-sciences company that develops and delivers effective oncology treatments using novel small particle technology. This effective new treatment delivers Selective Internal Radiation Therapy directly into the pancreas. Veltrane Medical Ltd is dedicated to delivering the latest innovations in radiotherapy treatments to ensure quality of life and the best possible care for pancreatic cancer patients. Veltrane Medical is utilising new technology to deliver safer radiotherapy treatments...<a href="#">more</a></p>

  <form class="signup abs">
    <div class="mail abs">
      <svg width="63" height="58" viewBox="0 0 63 58"><rect x="12" y="16" width="39" height="27" rx="2" fill="#e8f0f8" stroke="#3a7fc0" stroke-width="2"/><polyline points="12,17 31.5,32 51,17" fill="none" stroke="#3a7fc0" stroke-width="2"/></svg>
    </div>
    <h3 class="abs">SIGN UP, ITS FREE!</h3>
    <input type="text" value="Enter your name" style="top:34px" aria-label="Name">
    <input type="text" value="Enter email  address" style="top:64px" aria-label="Email">
    <div class="perk abs" style="top:96px"><svg width="14" height="12" viewBox="0 0 14 12"><polyline points="1,6 5,10 13,1" fill="none" stroke="#5aa02c" stroke-width="2.5"/></svg>Regular Updates</div>
    <div class="perk abs" style="top:114px"><svg width="14" height="12" viewBox="0 0 14 12"><polyline points="1,6 5,10 13,1" fill="none" stroke="#5aa02c" stroke-width="2.5"/></svg>Market Commentary</div>
    <div class="btn abs">REGISTER</div>
  </form>

  <div class="tab abs">WATCH VIDEOS</div>
  <a class="more-link abs">more &gt;&gt;</a>
  <div class="video-panel abs"></div>
  <div class="video abs" role="img" aria-label="Video still of a surgical team working in an operating theatre"></div>
  <div class="play abs"><svg width="36" height="36" viewBox="0 0 36 36"><polygon points="14,10 26,18 14,26" fill="#333"/></svg></div>
  <div class="video-bar abs">▶ 00:01 ━━━━━━━━━━━━━━━━━━━━━━━━━━━━ 100 ✕</div>
  <div class="thumb abs" style="top:721px" role="img" aria-label="Video thumbnail: surgical procedure"></div>
  <div class="thumb abs" style="top:767px" role="img" aria-label="Video thumbnail: laboratory equipment"></div>
  <div class="thumb abs" style="top:813px" role="img" aria-label="Video thumbnail: clinicians consulting"></div>
  <div class="thumb abs" style="top:860px" role="img" aria-label="Video thumbnail: patient treatment"></div>
  <div class="thumb abs" style="top:906px" role="img" aria-label="Video thumbnail: scan images"></div>

  <section class="services">
    <div class="services-title abs">
      <svg width="34" height="26" viewBox="0 0 34 26"><circle cx="10" cy="10" r="6" fill="none" stroke="#3a2f8f" stroke-width="4" stroke-dasharray="3 2"/><circle cx="24" cy="17" r="6" fill="none" stroke="#3a2f8f" stroke-width="4" stroke-dasharray="3 2"/></svg>
      <h2>Our Services</h2>
    </div>
    <div class="service abs" style="top:722px"><span class="ico"></span><p>Lorem ipsum dolor sit amet, consectetur adipisicing elit, sed do eiusmod tempor incididunt...<a href="#">more</a></p></div>
    <div class="service abs" style="top:774px"><span class="ico"></span><p>Lorem ipsum dolor sit amet, conse ctetur adipisicing elit, sed do eiusmod tempor incididunt...<a href="#">more</a></p></div>
    <div class="service abs" style="top:823px"><span class="ico"></span><p>Lorem ipsum dolor sit amet, consectetur adipisicing elit, sed do eiusmod tempor incidid...<a href="#">more</a></p></div>
    <div class="service abs" style="top:874px"><span class="ico"></span><p>Lorem ipsum dolor sit amet, consectetur adipisicing elit, sed do eiusmod tempor incidid...<a href="#">more</a></p></div>
    <div class="btn abs">+ READ MORE</div>
  </section>

  <footer class="footer abs">
    <div class="ask abs">Got some questions?  Need advice?<br>Get in touch with us!</div>
    <div class="f-brand abs"><span class="brand-dot"></span><span class="brand-name">Veltrane<br>Medical</span></div>
    <div class="office abs"><b>Melbourne Office</b><br>48 Harlow Lane, Suite 12, Carrow Park 3021</div>
    <div class="contact-grid abs">
      <b>Website</b><span>: veltrane.example</span><b>Email</b><span>: admin@veltrane.example</span>
      <b>Phone</b><span>: 00 4821 3307</span><b>Fax</b><span>: 00 4821 3307</span>
    </div>
    <div class="qn-title abs">Quick Navigation</div>
    <ul class="qn abs" style="left:640px"><li>Home</li><li>About Us</li><li>Products</li><li>Technology</li><li>Clinical Trials</li><li>Investors</li></ul>
    <ul class="qn abs" style="left:767px"><li>Newsroom</li><li>Join Us</li><li>Contact Us</li><li>FAQs</li><li>Webmail</li><li>Sitemap</li></ul>
    <div class="copyright abs">Copyrights © Veltrane Medical Ltd. 2013. All rights reserved. <a href="#">Privacy Policy</a> <a href="#">Disclaimer</a></div>
  </footer>

</div>
</body>
</html>
```